FC Blavin - Creation of a AD banner for our yearly event

We are a local soccer club in Switzerland. We're organizing a event that will substitute to our yearly club dinner. We need a banner AD to promote on the social networks this event.
We would like to see design that use one or the 2 colors of the club (blue and red).
This Ad should link to a online shop where we can buy vouchers.

Requirements
Must have
• Logo of the club
Title : Souper de gala quand même
Call to action : Plus d'informations
Side texte : Grande Tombola
Banner size : W300xH250 or W300xH600
Nice to have
• Promotion texte: Soutenez le FC Blavin et les restaurateurs locaux

```html
<!DOCTYPE html>
<html lang="fr">
<head>
<meta charset="utf-8">
<title>FC Blavin – Souper de gala quand même</title>
<link rel="stylesheet" href="https://fonts.googleapis.com/css2?family=Lilita+One&family=Roboto+Condensed:wght@700&display=swap">
<style>
  :root {
    --club-red: #e8323f;
    --club-blue: #1d8fd8;
    --ink: #1b1b1b;
    --white: #ffffff;
    --bg-light: #ffffff;
    --bg-edge: #e4e4e6;
  }
  html, body {
    margin: 0;
    padding: 0;
    width: 1200px;
    height: 2400px;
    overflow: hidden;
  }
  .banner {
    position: relative;
    width: 1200px;
    height: 2400px;
    overflow: hidden;
    background: radial-gradient(ellipse at 50% 55%, var(--bg-light) 0%, #f6f6f7 45%, var(--bg-edge) 100%);
    font-family: "Lilita One", sans-serif;
  }
  .club-name {
    position: absolute;
    top: 190px;
    left: 0;
    width: 100%;
    text-align: center;
    font-size: 150px;
    line-height: 1;
    color: var(--club-blue);
    letter-spacing: 2px;
  }
  .title {
    position: absolute;
    left: 0;
    width: 100%;
    margin: 0;
    text-align: center;
    font-weight: 400;
    font-size: 104px;
    line-height: 1;
    letter-spacing: 1px;
  }
  .title--red { top: 694px; color: var(--club-red); }
  .title--blue { top: 858px; color: var(--club-blue); }
  .cta {
    position: absolute;
    left: 152px;
    top: 1048px;
    width: 896px;
    height: 160px;
    border-radius: 48px;
    background: var(--ink);
    color: var(--white);
    font-family: "Roboto Condensed", sans-serif;
    font-weight: 700;
    font-size: 80px;
    line-height: 160px;
    text-align: center;
    text-decoration: none;
  }
  .ball-art {
    position: absolute;
    left: 230px;
    top: 1330px;
    width: 740px;
    height: 740px;
    border-radius: 50%;
    background: radial-gradient(circle, #f2f2f2 0%, #d9d9dc 30%, rgba(232,50,63,0.35) 55%, rgba(29,70,160,0.3) 72%, rgba(255,255,255,0) 100%);
  }
  .raffle {
    position: absolute;
    left: 360px;
    top: 2020px;
    width: 480px;
    height: 480px;
  }
  .raffle-text {
    position: absolute;
    left: 0;
    top: 2140px;
    width: 100%;
    text-align: center;
    color: var(--white);
    font-size: 66px;
    line-height: 98px;
  }
</style>
</head>
<body>
  <main class="banner">
    <div class="club-name">FC Blavin</div>

    <h1 class="title title--red">SOUPER DE GALA</h1>
    <h2 class="title title--blue">QUAND MÊME</h2>

    <a class="cta" href="#">Plus d'informations</a>

    <div class="ball-art" role="img" aria-label="Ballon de football entouré d'un tourbillon de points rouges et bleus"></div>

    <svg class="raffle" viewBox="0 0 480 480" aria-hidden="true">
      <g fill="#e8323f" transform="translate(240 240)">
        <rect x="-172" y="-172" width="344" height="344"/>
        <rect x="-172" y="-172" width="344" height="344" transform="rotate(22.5)"/>
        <rect x="-172" y="-172" width="344" height="344" transform="rotate(45)"/>
        <rect x="-172" y="-172" width="344" height="344" transform="rotate(67.5)"/>
      </g>
    </svg>
    <div class="raffle-text">GRANDE<br>TOMBOLA</div>
  </main>
</body>
</html>
```